Lumora Education - new College Consulting company in San Francisco needs a flyer design

We need a logo design for a new college admissions consulting business in San Francisco Bay Area and San Jose called 'Lumora Education'. We plan to develop tailor-made strategies for each students dreams and aspirations and will help provide them with online classes and in-person consulting starting Summer 2022.
Lumora Education plans on providing a free first time consulting to attract clients and grow our client base from there.
Lumora Education has a small team of consultants who have degrees from Economics/Business, Biology, and Computer Science who can provide tailored guidance to meet student and parent expectations and spend the time to walk them throughout the process.
Please refer to attached logos for the company and to create a flyer.
Target Market(s)
Competitive College Consulting
Industry/Entity Type
Education Consulting
Look and feel

```html
<!DOCTYPE html>
<html lang="en">
<head>
<meta charset="utf-8">
<title>Lumora Education – Free First Time Consulting</title>
<link href="https://fonts.googleapis.com/css2?family=Montserrat:wght@300;400;500;600;700;800&display=swap" rel="stylesheet">
<style>
  :root{
    --ink:#231f20;
    --coral:#f5897d;
    --coral-deep:#ef7468;
    --paper:#ffffff;
    --text:#2b2b2b;
    --muted:#555555;
    --title-red:#c8372b;
  }
  *{margin:0;padding:0;box-sizing:border-box}
  html,body{width:857px;height:1200px;overflow:hidden;background:var(--paper)}
  body{font-family:"Montserrat",Arial,sans-serif;color:var(--text)}
  .flyer{position:relative;width:857px;height:1200px;overflow:hidden;background:var(--paper)}
  .hero-shapes{position:absolute;left:0;top:0}
  .brand{position:absolute;left:40px;top:96px;color:var(--paper)}
  .brand-name{font-size:25px;font-weight:600;letter-spacing:.3px}
  .brand-tagline{font-size:19px;font-weight:400;margin-top:8px}
  .headline{position:absolute;left:50px;top:262px;color:var(--ink)}
  .headline .lead{font-size:42px;font-weight:400;color:var(--title-red);line-height:1.1}
  .headline .offer{font-size:50px;font-weight:700;line-height:1.12;margin-top:6px;color:var(--ink)}
  .services{position:absolute;left:51px;top:622px;width:380px}
  .section-title{font-size:33px;font-weight:700;color:var(--ink);letter-spacing:.3px}
  .services .intro{font-size:14.5px;line-height:1.5;margin-top:14px;color:var(--muted)}
  .service{display:flex;gap:22px;margin-top:26px}
  .service:first-of-type{margin-top:22px}
  .service-icon{width:54px;height:54px;flex:none;display:flex;align-items:center;justify-content:center}
  .service-icon.coral{background:var(--coral)}
  .service-icon.ink{background:var(--ink)}
  .service h3{font-size:20px;font-weight:600;color:var(--ink);margin-top:2px}
  .service p{font-size:14px;line-height:1.45;color:var(--muted);margin-top:6px}
  .why{position:absolute;left:469px;top:708px;width:370px}
  .sub-title{font-size:20px;font-weight:600;color:var(--ink);letter-spacing:.3px}
  .why p,.about p{font-size:13px;line-height:1.5;color:var(--muted);margin-top:10px}
  .why ul{list-style:none;margin-top:14px}
  .why li{font-size:11px;letter-spacing:-.15px;white-space:nowrap;color:var(--muted);display:flex;align-items:center;gap:12px;height:26px}
  .why li::before{content:"";width:9px;height:9px;background:var(--coral-deep);flex:none}
  .about{position:absolute;left:469px;top:952px;width:370px}
  .footer-shapes{position:absolute;left:0;top:1098px}
  .footer-cta{position:absolute;left:51px;top:1120px;color:var(--paper)}
  .footer-cta .small{font-size:21px;font-weight:400}
  .footer-cta .big{font-size:27px;font-weight:700;margin-top:6px}
  .contact{position:absolute;right:108px;top:1120px;text-align:right;color:var(--paper)}
  .contact .small{font-size:21px;font-weight:400}
  .contact .phone{font-size:26px;font-weight:500;margin-top:6px}
  .contact-icon{position:absolute;right:32px;top:1122px}
</style>
</head>
<body>
<div class="flyer">
  <svg class="hero-shapes" width="857" height="680" viewBox="0 0 857 680">
    <defs>
      <linearGradient id="photoTone" x1="0" y1="0" x2="1" y2="1">
        <stop offset="0" stop-color="#c9b29a"/>
        <stop offset=".5" stop-color="#9a8470"/>
        <stop offset="1" stop-color="#6f6a66"/>
      </linearGradient>
    </defs>
    <path d="M288 470 Q296 668 500 668 L536 640 H470 Q330 640 330 500 Z" fill="var(--coral)"/>
    <path d="M330 0 H857 V640 H470 Q330 640 330 500 Z" fill="url(#photoTone)" role="img" aria-label="Photo of two smiling students walking together on a college campus"/>
    <polygon points="0,78 418,78 388,192 0,192" fill="var(--ink)"/>
    <polygon points="0,232 300,232 428,395 428,540 0,540" fill="var(--coral)"/>
    <polygon points="0,540 428,540 440,555 0,555" fill="var(--ink)"/>
  </svg>

  <div class="brand">
    <div class="brand-name">Lumora Education</div>
    <div class="brand-tagline">Learning is a phenomenom</div>
  </div>

  <div class="headline">
    <div class="lead">We Provide</div>
    <div class="offer">Free<br>First Time<br>Consulting</div>
  </div>

  <section class="services">
    <h2 class="section-title">OUR SERVICES</h2>
    <p class="intro">Lorem ipsum dolor sit amet, consectetur adipisicing elit, sed do eiusmod tempor incididunt</p>

    <div class="service">
      <div class="service-icon coral">
        <svg width="28" height="28" viewBox="0 0 28 28" fill="none" stroke="#fff" stroke-width="2.4"><path d="M4 24 H24"/><rect x="6" y="14" width="4" height="8" fill="#fff"/><rect x="12" y="10" width="4" height="12" fill="#fff"/><rect x="18" y="5" width="4" height="17" fill="#fff"/></svg>
      </div>
      <div><h3>ECONOMICS/BUSINESS</h3><p>Nemo enim ipsam voluptatem quia voluptas sit aspernatur.</p></div>
    </div>

    <div class="service">
      <div class="service-icon ink">
        <svg width="28" height="28" viewBox="0 0 28 28" fill="none" stroke="#fff" stroke-width="2.2"><circle cx="14" cy="14" r="10"/><circle cx="14" cy="14" r="3.5"/></svg>
      </div>
      <div><h3>BIOLOGY</h3><p>Nemo enim ipsam voluptatem quia voluptas sit aspernatur.</p></div>
    </div>

    <div class="service">
      <div class="service-icon coral">
        <svg width="28" height="28" viewBox="0 0 28 28" fill="none" stroke="#fff" stroke-width="2.2"><rect x="4" y="5" width="20" height="14" rx="1.5"/><path d="M10 24 H18 M14 19 V24"/></svg>
      </div>
      <div><h3>COMPUTER SCIENCE</h3><p>Nemo enim ipsam voluptatem quia voluptas sit aspernatur.</p></div>
    </div>
  </section>

  <section class="why">
    <h2 class="sub-title">WHY CHOOSE US?</h2>
    <p>Lorem ipsum dolor sit amet, consectetur adipisicing elit, sed do eiusmod</p>
    <ul>
      <li>Lorem ipsum dolor sit amet, consectetur adipisicing elit</li>
      <li>Lorem ipsum dolor sit amet, consectetur adipisicing elit</li>
      <li>Lorem ipsum dolor sit amet, consectetur adipisicing elit</li>
      <li>Lorem ipsum dolor sit amet, consectetur adipisicing elit</li>
      <li>Lorem ipsum dolor sit amet, consectetur adipisicing elit</li>
    </ul>
  </section>

  <section class="about">
    <h2 class="sub-title">ABOUT OUR COLLEGE</h2>
    <p>Lorem ipsum dolor sit amet, consectetur a adipisicing elit, sed do eiusmod tempor incididunt ut labore et dolore magna aliqua. Quis ipsum suspendisse ultrices</p>
  </section>

  <svg class="footer-shapes" width="857" height="102" viewBox="0 0 857 102">
    <rect x="0" y="0" width="857" height="102" fill="var(--ink)"/>
    <path d="M500 0 H857 V102 H430 Q470 90 470 50 Q470 0 500 0 Z" fill="var(--coral)"/>
  </svg>

  <div class="footer-cta">
    <div class="small">Get Your</div>
    <div class="big">Free Consultations</div>
  </div>

  <div class="contact">
    <div class="small">More info</div>
    <div class="phone">+000 123 456 789</div>
  </div>

  <svg class="contact-icon" width="60" height="56" viewBox="0 0 60 56" fill="none" stroke="#fff" stroke-width="3.5">
    <path d="M30 5 C45 5 55 13 55 24 C55 35 45 43 30 43 C26 43 22 42 19 41 L8 49 L11 37 C7 34 5 29 5 24 C5 13 15 5 30 5 Z"/>
    <path d="M18 20 H42 M18 28 H36"/>
  </svg>
</div>
</body>
</html>
```